Shoes, Handbags and Accessories

The main business of the company are shoes and then handbags, jewellery and scarves to accessorize.

The design I am looking for is a "shabby chic" design, cursive font, perhaps with a vintage country feel to it.

Target Market(s)

Age group are more for the 25+, but more so 35+ ladies.

Industry/Entity Type

Business

Contact Information for Business Card

Lantern Row Boutique & Accessories
Marcia Pellbrook - P.O. Box 482, Yarrabin W.A. 6391
Ph: (08) 97213356 fax: (08) 97213374 Mobile: 0419382716
Email:lanternrow@quillnet.com.au
Web: www.lanternrowboutique.com.au
Like us on socialpage (socialpage logo)

Requirements
Must have
• As already described. A "faded" picture background is also another feature I like, but I don't want to create a cluttered look about the business card.
Nice to have
• Classy, stylish and comfortable shoes.

```html
<!DOCTYPE html>
<html lang="en">
<head>
<meta charset="utf-8">
<title>Lantern Row Boutique &amp; Accessories – Business Card</title>
<link href="https://fonts.googleapis.com/css2?family=Pinyon+Script&family=Noto+Serif:wght@700&family=Open+Sans:wght@400&display=swap" rel="stylesheet">
<style>
  :root {
    --backdrop: #e9e6e1;
    --card-white: #fbfaf8;
    --wood-tan: #dfc08d;
    --wood-light: #efe1c6;
    --ink-brown: #4a2e14;
    --text-dark: #2d2a26;
    --icon-brown: #7a5a2c;
    --shoe-beige: #c9b08a;
    --shoe-wine: #5e2226;
    --shoe-slate: #5b5b5e;
  }
  * { box-sizing: border-box; margin: 0; padding: 0; }
  html, body {
    width: 1200px; height: 918px; overflow: hidden;
    background: var(--backdrop);
  }
  .business-card {
    position: absolute; left: 75px; top: 159px;
    width: 1050px; height: 600px;
    background: linear-gradient(180deg, var(--wood-tan) 0%, var(--wood-light) 28%, var(--card-white) 52%, var(--card-white) 100%);
    box-shadow: 0 6px 24px rgba(0,0,0,.18);
    overflow: hidden;
  }
  .brand-name {
    position: absolute; left: 120px; top: 34px;
    font-family: "Pinyon Script", cursive;
    font-weight: 400;
    color: var(--ink-brown);
    line-height: 1;
  }
  .brand-name .brand-line { display: block; font-size: 76px; }
  .brand-name .brand-sub { display: block; font-size: 64px; margin: 6px 0 0 110px; }
  .contact-block {
    position: absolute; left: 110px; top: 250px;
    color: var(--text-dark);
  }
  .contact-name {
    font-family: "Noto Serif", serif; font-weight: 700;
    font-size: 38px; line-height: 46px; color: var(--ink-brown);
    margin-bottom: 6px;
  }
  .contact-line {
    font-family: "Open Sans", sans-serif;
    font-size: 20px; line-height: 27px;
    white-space: nowrap;
  }
  .social-block {
    position: absolute; right: 80px; top: 250px;
    display: flex; align-items: center; gap: 16px;
    font-family: "Open Sans", sans-serif; font-size: 22px;
    color: var(--text-dark); line-height: 1.2;
  }
  .social-square {
    width: 64px; height: 64px; border-radius: 6px;
    background: var(--icon-brown);
  }
  .product-row {
    position: absolute; left: 0; right: 0; bottom: 28px; height: 72px;
  }
  .product-photo {
    position: absolute; bottom: 0; width: 150px; height: 68px;
    border-radius: 36px 44px 10px 18px;
  }
  .product-photo.boot { left: 200px; background: radial-gradient(ellipse at 40% 60%, #77777a, var(--shoe-slate) 70%); }
  .product-photo.heel { left: 500px; background: radial-gradient(ellipse at 40% 60%, #7a3236, var(--shoe-wine) 70%); }
  .product-photo.pump { left: 800px; background: radial-gradient(ellipse at 40% 60%, #dcc6a2, var(--shoe-beige) 70%); }
</style>
</head>
<body>
  <main class="business-card">
    <h1 class="brand-name">
      <span class="brand-line">Lantern Row Boutique</span>
      <span class="brand-sub">&amp; Accessories</span>
    </h1>

    <section class="contact-block">
      <h2 class="contact-name">Marcia Pellbrook</h2>
      <p class="contact-line">P.O. Box 482, Yarrabin W.A. 6391</p>
      <p class="contact-line">Ph: (08) 97213356 fax: (08) 97213374</p>
      <p class="contact-line">Mobile: 0419382716</p>
      <p class="contact-line">Email:lanternrow@quillnet.com.au</p>
      <p class="contact-line">Web: www.lanternrowboutique.com.au</p>
    </section>

    <aside class="social-block">
      <p class="social-text">Like us on<br>socialpage</p>
      <div class="social-square"></div>
    </aside>

    <div class="product-row">
      <div class="product-photo boot" role="img" aria-label="Photo of a grey leather ankle boot"></div>
      <div class="product-photo heel" role="img" aria-label="Photo of a burgundy buckled heeled shoe"></div>
      <div class="product-photo pump" role="img" aria-label="Photo of a beige peep-toe pump"></div>
    </div>
  </main>
</body>
</html>
```